Stationary/business card design for Harborline Building Partners
Harborline Building Partners
Stationary/business card design for Harborline Building Partners - Consulting
Creative Brief
Use specific fonts
Up to designer. Can be different from logo if that looks good.
Simple
Clara T Revanski
Director - Business Development & Support
3870 Wexmoor Avenue - Suite 2C Rochester, NY 14618
clara.revanski@hbpworkline.com
www.HBPworkline.com
The back of the business card will have some of what we do on there, for example: GIS, Drafting, Master Data. I haven't written that up yet.

```html
<!DOCTYPE html>
<html lang="en">
<head>
<meta charset="utf-8">
<title>Harborline Building Partners – Stationery Concepts</title>
<link href="https://fonts.googleapis.com/css2?family=Montserrat:wght@400;600&family=Open+Sans:wght@400&display=swap" rel="stylesheet">
<style>
  :root {
    --green: #1aa33a;
    --green-dark: #12802c;
    --ink: #111111;
    --paper: #ffffff;
    --stage: #ececec;
    --label: #6e6e6e;
    --fine: #8a8a8a;
    --ghost: rgba(26, 163, 58, 0.12);
  }
  * { box-sizing: border-box; margin: 0; padding: 0; }
  html, body { width: 1200px; height: 446px; overflow: hidden; }
  body {
    background: var(--stage);
    font-family: "Open Sans", sans-serif;
    position: relative;
  }
  .label {
    position: absolute;
    font-family: "Montserrat", sans-serif;
    font-size: 6px;
    letter-spacing: 1px;
    text-transform: uppercase;
    color: var(--label);
    white-space: nowrap;
  }
  .sheet {
    position: absolute;
    background: var(--paper);
    box-shadow: 0 1px 4px rgba(0,0,0,0.18);
    overflow: hidden;
  }
  .sheet svg.trim { position: absolute; inset: 0; width: 100%; height: 100%; }
  .brand {
    position: absolute;
    font-family: "Montserrat", sans-serif;
    font-weight: 600;
    color: var(--green);
    line-height: 1.05;
    display: flex;
    align-items: center;
    gap: 4px;
  }
  .brand .mark { width: 9px; height: 9px; background: var(--green); flex: none; }
  .business-card .brand { gap: 2px; }
  .business-card .brand .mark { width: 5px; height: 5px; }
  .contact {
    position: absolute;
    font-size: 4.2px;
    line-height: 1.55;
    color: var(--fine);
    white-space: nowrap;
  }
  .ghost-name {
    position: absolute;
    font-family: "Montserrat", sans-serif;
    font-weight: 600;
    color: var(--ghost);
    text-align: center;
    line-height: 1;
  }
</style>
</head>
<body>

  <div class="label" style="left:12px;top:124px;">Stationery Concepts</div>

  <!-- Business card front -->
  <div class="sheet business-card" style="left:12px;top:158px;width:58px;height:68px;">
    <svg class="trim" viewBox="0 0 58 68" preserveAspectRatio="none" aria-hidden="true">
      <path d="M0 0 H6 C2 24 3 48 13 68 H0 Z" fill="var(--green)"/>
      <path d="M6 0 C2 24 3 48 13 68" stroke="var(--ink)" stroke-width="1" fill="none"/>
    </svg>
    <div class="brand" style="left:15px;top:8px;font-size:4.4px;width:40px;"><span class="mark"></span>Harborline Building Partners</div>
    <div class="contact" style="left:15px;top:30px;font-size:2.6px;">
      Clara T Revanski<br>Director - Business Development &amp; Support<br>3870 Wexmoor Avenue - Suite 2C<br>Rochester, NY 14618<br>clara.revanski@hbpworkline.com<br>www.HBPworkline.com
    </div>
  </div>
  <div class="label" style="left:14px;top:232px;font-size:4.5px;">Business Card Front</div>

  <!-- Business card back -->
  <div class="sheet business-card-back" style="left:12px;top:254px;width:58px;height:56px;background:var(--green);"></div>
  <div class="label" style="left:14px;top:316px;font-size:4.5px;">Business Card Back</div>

  <!-- Letterhead option 1 -->
  <div class="sheet letterhead" style="left:161px;top:12px;width:242px;height:415px;">
    <svg class="trim" viewBox="0 0 242 415" preserveAspectRatio="none" aria-hidden="true">
      <path d="M0 0 H26 C12 140 10 300 70 415 H0 Z" fill="var(--green)"/>
      <path d="M26 0 C12 140 10 300 70 415" stroke="var(--ink)" stroke-width="3" fill="none"/>
    </svg>
    <div class="brand" style="left:40px;top:18px;font-size:10px;width:110px;"><span class="mark"></span>Harborline Building Partners</div>
    <div class="contact" style="left:152px;top:16px;">
      3870 Wexmoor Avenue - Suite 2C<br>Rochester, NY 14618<br>Office 585.555.0142<br>clara.revanski@hbpworkline.com<br>www.HBPworkline.com
    </div>
    <div class="ghost-name" style="left:50px;top:150px;width:170px;font-size:30px;">Harborline Building Partners</div>
  </div>
  <div class="label" style="left:220px;top:434px;">Letterhead Option 1</div>

  <!-- Letterhead option 2 -->
  <div class="sheet letterhead" style="left:422px;top:12px;width:243px;height:415px;">
    <svg class="trim" viewBox="0 0 243 415" preserveAspectRatio="none" aria-hidden="true">
      <path d="M0 0 H18 C6 160 14 320 90 415 H0 Z" fill="var(--green)"/>
      <path d="M18 0 C6 160 14 320 90 415" stroke="var(--ink)" stroke-width="3" fill="none"/>
    </svg>
    <div class="brand" style="left:40px;top:18px;font-size:10px;width:110px;"><span class="mark"></span>Harborline Building Partners</div>
    <div class="contact" style="left:152px;top:16px;">
      3870 Wexmoor Avenue - Suite 2C<br>Rochester, NY 14618<br>Office 585.555.0142<br>clara.revanski@hbpworkline.com<br>www.HBPworkline.com
    </div>
    <div class="ghost-name" style="left:50px;top:150px;width:170px;font-size:30px;">Harborline Building Partners</div>
  </div>
  <div class="label" style="left:480px;top:434px;">Letterhead Option 2</div>

  <!-- Envelope option 1: flaps -->
  <div class="sheet envelope" style="left:696px;top:12px;width:494px;height:84px;">
    <svg class="trim" viewBox="0 0 494 84" preserveAspectRatio="none" aria-hidden="true">
      <rect width="494" height="14" fill="var(--green)"/>
      <path d="M0 14 L247 60 L494 14" stroke="var(--ink)" stroke-width="1" fill="none"/>
    </svg>
  </div>
  <div class="sheet envelope" style="left:696px;top:100px;width:494px;height:84px;background:var(--ink);">
    <svg class="trim" viewBox="0 0 494 84" preserveAspectRatio="none" aria-hidden="true">
      <path d="M0 0 L247 48 L494 0 Z" fill="#222"/>
      <path d="M0 0 L247 48 L494 0" stroke="var(--green)" stroke-width="1.5" fill="none"/>
    </svg>
  </div>
  <div class="sheet envelope" style="left:696px;top:188px;width:494px;height:84px;">
    <svg class="trim" viewBox="0 0 494 84" preserveAspectRatio="none" aria-hidden="true">
      <path d="M0 0 L247 36 L494 0" stroke="#cfcfcf" stroke-width="1" fill="none"/>
    </svg>
    <div class="brand" style="left:200px;top:42px;font-size:8px;"><span class="mark"></span>Harborline Building Partners</div>
  </div>
  <div class="label" style="left:900px;top:278px;">Envelope Option 1</div>

  <!-- Envelope option 2: front -->
  <div class="sheet envelope-front" style="left:696px;top:292px;width:494px;height:130px;">
    <div class="brand" style="left:14px;top:12px;font-size:8px;width:120px;"><span class="mark"></span>Harborline Building Partners</div>
    <div class="contact" style="left:138px;top:12px;">
      3870 Wexmoor Avenue - Suite 2C<br>Rochester, NY 14618
    </div>
    <div class="ghost-name" style="left:300px;top:60px;width:190px;font-size:22px;">Harborline Building Partners</div>
  </div>
  <div class="label" style="left:900px;top:430px;">Envelope Option 2</div>

</body>
</html>
```